Harbour Gale Cooler - Velmora Distillery

We need help designing a label for a Ready To Drink (RTD) canned beverage called "Harbour Gale Cooler".

We are a Distillery in Bunbury, Western Australia and you have done a canned beer label design work for a place called Tallick Brewery who we are working together with on the "Harbour Gale Cooler" (using their ginger beer). I have attached the Label you used for them titled Tallick Spiced Fizz Can. You can use that for sizing at it will be the pretty much the same size just very marginally bigger.

We are called Velmora Distillery as Velmora is the latin word for Copper and all our stills are copper pot stills that we use to make the spirits. The can itself will likely be copper colour with a black lid.

We really have no real specific direction we want to go in so certainly leaving the artistic creativity to you guys. There's a few different concepts i would like to see created.

We have done a Rum label before (rum bottle attached) called Admiral Lantern Pure Single Rum and we we were hoping to use somewhat similar style artwork on the can. However, instead of the words Pure, Single, Rum along the banner we were hoping to have "Harbour Gale Cooler" instead. Depending on pricing we may have the words on the badge metallic or slightly raised. My only concern with that is the Admiral Lantern character would not be big enough so he would need to be redesigned to be larger and perhaps looking like he is coming out of the can or something. (hope that makes sense)

Another concept would be a doing a literal storm theme throughout. Like have a ship in rocky waters with lightning bolts and a more dark and broody theme to it or a washed up shipwreck during a storm.

As for the boring stuff... see how the Tallick spiced fizz label is divided into somewhat three sections. We would like the blurb section to be slightly smaller area and the front/first section to be larger. I have attached the new barcode. I have also attached our QR code that we would want on there, the can will have the same mls - 375 however the ABV% will be 4.5% which means we need the standard drinks logo to change to 1.3. Pregnancy label kept the same and I will finalise the blurb once we have the flavour profile (in the coming days) however this will be a similar length. Remove the text at the bottom and the canning details may look neater in a small paragraph rather than down one side,

The middle section instead of a large Tallick logo it needs to be a smaller version without the "poured with purpose" part then "x" then our logo which is attached and underneath running across both logos text saying "Working together for the heart of the coast"

Kind regards,
Denis from Velmora Distillery

Requirements
Must have
• Harbour Gale Cooler on the front of the can (this is name of the drink)

```html
<!DOCTYPE html>
<html lang="en">
<head>
<meta charset="utf-8">
<title>Harbour Gale Cooler – Label</title>
<link rel="stylesheet" href="https://fonts.googleapis.com/css2?family=Montserrat:wght@500;700&display=swap">
<style>
  :root {
    --bg: #e2e2e2;
    --paper: #ffffff;
    --ink: #151515;
    --copper: #d2693a;
    --copper-light: #f0a57c;
    --rust: #8e3f22;
    --bark: #5a2c18;
  }
  html, body {
    margin: 0;
    width: 1200px;
    height: 1200px;
    overflow: hidden;
    background: var(--bg);
    font-family: "Montserrat", sans-serif;
  }
  .canvas {
    position: relative;
    width: 1200px;
    height: 1200px;
  }

  /* Neck label */
  .neck-label {
    position: absolute;
    left: 300px;
    top: 120px;
    width: 600px;
    height: 150px;
    background: var(--paper);
    box-shadow: 0 2px 10px rgba(0,0,0,.08);
    display: flex;
    align-items: center;
    justify-content: center;
    color: var(--ink);
  }
  .neck-name {
    font-weight: 700;
    font-size: 34px;
    letter-spacing: 4px;
    text-transform: uppercase;
    line-height: 1;
  }

  /* Body label */
  .body-label {
    position: absolute;
    left: 120px;
    top: 340px;
    width: 960px;
    height: 620px;
    background: linear-gradient(180deg, var(--copper) 0%, var(--rust) 55%, var(--bark) 100%);
    overflow: hidden;
    box-shadow: 0 2px 14px rgba(0,0,0,.1);
  }
  .front-panel {
    position: absolute;
    left: 230px;
    top: 0;
    width: 500px;
    height: 520px;
    background: var(--paper);
    border-radius: 0 0 250px 250px;
  }
  .wheat-art {
    position: absolute;
    left: 250px;
    top: 90px;
    width: 460px;
    height: 420px;
    border-radius: 0 0 230px 230px;
    background: radial-gradient(circle at 50% 60%, rgba(240,165,124,.35), rgba(240,165,124,0) 70%);
  }
  .product-name {
    position: absolute;
    left: 230px;
    top: 170px;
    width: 500px;
    margin: 0;
    text-align: center;
    color: var(--ink);
    font-weight: 700;
    font-size: 62px;
    line-height: 1.08;
    letter-spacing: 6px;
    text-transform: uppercase;
  }
  .product-name span { display: block; }

  .side-blurb {
    position: absolute;
    left: 780px;
    top: 40px;
    width: 140px;
    margin: 0;
    color: var(--paper);
    font-size: 13px;
    line-height: 1.5;
    font-weight: 500;
    text-transform: uppercase;
  }
  .badges {
    position: absolute;
    left: 790px;
    top: 300px;
    display: flex;
    flex-direction: column;
    gap: 14px;
  }
  .badge-square {
    width: 56px; height: 56px;
    background: var(--paper);
    border-radius: 6px;
  }
  .badge-circle {
    width: 56px; height: 56px;
    background: var(--paper);
    border-radius: 50%;
  }
  .left-accent {
    position: absolute;
    left: 40px;
    top: 180px;
    width: 150px;
    height: 150px;
    border: 6px solid var(--paper);
    border-radius: 50%;
    opacity: .7;
  }

  .ingredient-band {
    position: absolute;
    left: 0;
    bottom: 50px;
    width: 100%;
    height: 34px;
    border-top: 4px solid var(--paper);
    border-bottom: 4px solid var(--paper);
    display: flex;
    align-items: center;
    justify-content: center;
    color: var(--paper);
    font-size: 14px;
    font-weight: 500;
    letter-spacing: 1px;
    text-transform: uppercase;
  }
</style>
</head>
<body>
  <main class="canvas">
    <section class="neck-label">
      <div class="neck-name">Harbour Gale Cooler</div>
    </section>

    <section class="body-label">
      <div class="left-accent"></div>
      <div class="front-panel"></div>
      <div class="wheat-art" role="img" aria-label="Soft wheat stalk illustration in copper tones"></div>
      <h1 class="product-name"><span>Harbour</span><span>Gale</span><span>Cooler</span></h1>
      <p class="side-blurb">Bright ginger, clean finish, coastal spirit.</p>
      <div class="badges">
        <div class="badge-square"></div>
        <div class="badge-circle"></div>
      </div>
      <div class="ingredient-band">Ingredients: water, cane sugar, ginger concentrate, yeast /// Malt: pale ale /// Hops: aromatic</div>
    </section>
  </main>
</body>
</html>
```